Business Association needs street banner design promoting business district.

We are a business association that manages a commercial district of small family owned businesses. We would like to install banners (30 inches wide by 60 inches long) on street lights. The banners will include our logo and the name of the sponsor (we will need a space for the sponsor information). We will also need a space to include a photo of the sponsoring business (this space needs to be large). The banners are intended to promote the local small businesses. For more information on our organization, our web site is www.fernmoorba.org.

Target Market(s)

Member businesses and customers.

Industry/Entity Type

Small Business

Font styles to use
Sans Serif

Requirements
Must have
• Any images or type must be large enough for pedestrians to read from a distance. Brights colors. No copy 4 inches from top or bottom (the banners will be folded and sewn). These banners will be installed on street lights (see example image in files). Please design banner in Adobe Illustrator.
• Text on banner: "Welcome to Fernmoor!" Please include logo on banner.

```html
<!DOCTYPE html>
<html lang="en">
<head>
<meta charset="utf-8">
<title>Welcome to Fernmoor – Street Banner</title>
<link rel="stylesheet" href="https://fonts.googleapis.com/css2?family=Roboto+Condensed:wght@700&family=Arimo:wght@400;700&display=swap">
<style>
  :root {
    --brand-blue: #2657a7;
    --accent-orange: #f9a72b;
    --paper: #ffffff;
    --ink: #333333;
    --placeholder-gray: #bcbfc2;
    --frame-line: #8f959b;
    --mist-blue: rgba(214, 223, 240, 0.9);
    --mist-fade: rgba(214, 223, 240, 0.45);
    --mist-clear: rgba(214, 223, 240, 0);
  }
  * { margin: 0; padding: 0; box-sizing: border-box; }
  html, body {
    width: 1200px;
    height: 959px;
    overflow: hidden;
    background: var(--paper);
  }
  .canvas {
    position: relative;
    width: 1200px;
    height: 959px;
    background: var(--paper);
  }
  .banner {
    position: absolute;
    left: 359px;
    top: 0;
    width: 478px;
    height: 959px;
    background: var(--paper);
    overflow: hidden;
  }
  .banner__backdrop {
    position: absolute;
    top: 560px;
    width: 240px;
    height: 520px;
    background: radial-gradient(ellipse closest-side at 50% 50%, var(--mist-blue) 0%, var(--mist-fade) 55%, var(--mist-clear) 100%);
  }
  .banner__backdrop--left { left: -120px; }
  .banner__backdrop--right { right: -120px; }
  .pennant {
    position: absolute;
    left: 0;
    top: 0;
    width: 478px;
    height: 252px;
  }
  .headline {
    position: absolute;
    left: 0;
    top: 84px;
    width: 478px;
    text-align: center;
    color: var(--paper);
    font-family: "Roboto Condensed", "Arial Narrow", sans-serif;
    font-weight: 700;
    text-transform: uppercase;
    line-height: 1;
  }
  .headline__lead {
    display: block;
    font-size: 51px;
    letter-spacing: 0.5px;
  }
  .headline__place {
    display: block;
    font-size: 72px;
    margin-top: 2px;
  }
  .sponsor-frame {
    position: absolute;
    left: 47px;
    top: 283px;
    width: 383px;
    height: 409px;
    background: var(--brand-blue);
  }
  .sponsor-photo {
    position: absolute;
    left: 11px;
    top: 15px;
    width: 361px;
    height: 241px;
    background: var(--paper);
    border: 2px solid var(--frame-line);
    display: flex;
    align-items: center;
    justify-content: center;
    font-family: "Arimo", Arial, sans-serif;
    font-size: 41px;
    color: var(--ink);
  }
  .sponsor-info {
    position: absolute;
    left: 11px;
    top: 271px;
    width: 361px;
    height: 126px;
    background: var(--paper);
    border: 2px solid var(--frame-line);
  }
  .sponsor-info__logo {
    position: absolute;
    left: 9px;
    top: 10px;
    width: 85px;
    height: 101px;
    background: var(--placeholder-gray);
    display: flex;
    align-items: center;
    justify-content: center;
    font-family: "Arimo", Arial, sans-serif;
    font-size: 20px;
    color: var(--ink);
  }
  .sponsor-info__text {
    position: absolute;
    left: 112px;
    right: 10px;
    top: 0;
    bottom: 0;
    display: flex;
    align-items: center;
    justify-content: center;
    font-family: "Arimo", Arial, sans-serif;
    font-size: 20px;
    color: var(--ink);
    text-transform: uppercase;
  }
  .association {
    position: absolute;
    left: 0;
    top: 726px;
    width: 478px;
    text-align: center;
  }
  .association__mark {
    display: block;
    width: 68px;
    height: 68px;
    margin: 0 auto;
    border-radius: 50%;
    background: var(--accent-orange);
  }
  .association__name {
    margin-top: 14px;
    font-family: "Arimo", Arial, sans-serif;
    font-weight: 700;
    font-size: 19px;
    line-height: 1.1;
    color: var(--ink);
    text-transform: uppercase;
  }
  .hem-tab {
    position: absolute;
    left: 191px;
    top: 894px;
    width: 93px;
    height: 80px;
    background: var(--paper);
    border: 1px solid var(--frame-line);
  }
</style>
</head>
<body>
  <main class="canvas">
    <section class="banner" aria-label="Street banner: Welcome to Fernmoor">
      <div class="banner__backdrop banner__backdrop--left" role="img" aria-label="Faint blue decorative swirl"></div>
      <div class="banner__backdrop banner__backdrop--right" role="img" aria-label="Faint blue decorative swirl"></div>

      <svg class="pennant" viewBox="0 0 478 252" aria-hidden="true">
        <polygon points="0,0 478,0 478,212 239,251 0,212" fill="var(--accent-orange)"/>
        <polygon points="0,0 478,0 478,192 239,238 0,192" fill="var(--brand-blue)"/>
      </svg>

      <h1 class="headline">
        <span class="headline__lead">Welcome to</span>
        <span class="headline__place">Fernmoor!</span>
      </h1>

      <div class="sponsor-frame">
        <div class="sponsor-photo">PHOTO</div>
        <div class="sponsor-info">
          <div class="sponsor-info__logo">LOGO</div>
          <div class="sponsor-info__text">Information</div>
        </div>
      </div>

      <div class="association">
        <span class="association__mark" aria-hidden="true"></span>
        <p class="association__name">Fernmoor<br>Business Association</p>
      </div>

      <div class="hem-tab" aria-hidden="true"></div>
    </section>
  </main>
</body>
</html>
```